Business card design needed

I need a business card for my new Food & Lifestyle Coaching business - "Bloomvale Food & Lifestlye Coaching"

i already have a logo and would like to have that incorporated into the business card, obviously.

i would like a design that says "fresh" and "funky" - my target market is female, aged 20-45 so i want something that will stand out to them when they see it.

My "Company Colour" is Apple Green
Updates

Thankyou to everyone who has submitted a design for my project. At this stage i have quite a large number of designs to chose from and with only a short time until my project closes i am focusing now on chosing from those i have already shortlisted so am unfortunately not considering any new desings.

Thankyou again for your interest in my project.

Target Market(s)

Female, Health Conscious (or looking to improve their health/lifestyle), aged between 20-45

Industry/Entity Type

Business

Contact Information for Business Card

Tamsin Corley
Ph: 0417382946
Email: eatwell@marovex.com

Requirements
Must have
• Must include my existing Logo
Nice to have
• Would be nice to incoirporate and appointment card on the back

```html
<!DOCTYPE html>
<html lang="en">
<head>
<meta charset="utf-8">
<title>Bloomvale Food &amp; Lifestyle Coaching – Business Card</title>
<link rel="stylesheet" href="https://fonts.googleapis.com/css2?family=PT+Sans:wght@400;700&family=Gochi+Hand&display=swap">
<style>
  :root {
    --apple-green: #84fc08;
    --leaf-green: #8ee61a;
    --ink: #1a1a1a;
    --paper: #ffffff;
    --backdrop-light: #c9cdbb;
    --backdrop-dark: #8d9478;
    --card-shadow: rgba(0, 0, 0, 0.55);
  }
  * { margin: 0; padding: 0; box-sizing: border-box; }
  html, body { width: 1200px; height: 900px; overflow: hidden; }
  body {
    background: radial-gradient(ellipse at 42% 48%, var(--backdrop-light) 0%, var(--backdrop-dark) 85%);
    font-family: "PT Sans", sans-serif;
    position: relative;
  }
  .card {
    position: absolute;
    left: 349px;
    width: 502px;
    height: 324px;
    border-radius: 24px;
    box-shadow: 4px 5px 6px var(--card-shadow);
    overflow: hidden;
  }
  .card--front { top: 107px; background: var(--paper); }
  .card--back { top: 482px; background: var(--apple-green); }

  .brand { position: absolute; left: 0; top: 0; width: 100%; height: 100%; }
  .brand__mark {
    position: absolute; left: 70px; top: 108px;
    width: 84px; height: 84px; border-radius: 50%;
    background: var(--leaf-green);
  }
  .brand__name {
    position: absolute; left: 172px; top: 124px;
    font-size: 60px; font-weight: 400; color: var(--ink);
    line-height: 1; letter-spacing: -0.5px;
    white-space: nowrap;
  }
  .brand__tagline {
    position: absolute; left: 240px; top: 210px;
    font-size: 15px; color: var(--ink);
    white-space: nowrap;
  }
  .brand__rule { position: absolute; left: 150px; top: 234px; }

  .contact {
    position: absolute; left: 30px; top: 26px;
    color: var(--ink); font-size: 18px; line-height: 25px;
  }
  .contact__name { font-weight: 700; }

  .appointment__label {
    position: absolute; left: 30px; top: 228px;
    color: var(--paper); font-size: 15px;
  }
  .appointment__date {
    position: absolute; left: 38px; top: 254px;
    font-family: "Gochi Hand", cursive;
    font-size: 28px; line-height: 1.1; color: var(--ink); letter-spacing: 1px;
    white-space: nowrap;
  }
  .appointment__rule { position: absolute; left: 34px; top: 284px; }
</style>
</head>
<body>
  <section class="card card--front">
    <div class="brand">
      <span class="brand__mark"></span>
      <div class="brand__name">Bloomvale</div>
      <div class="brand__tagline">Food &amp; Lifestyle Coaching</div>
      <svg class="brand__rule" width="280" height="6" viewBox="0 0 280 6">
        <line x1="0" y1="3" x2="278" y2="3" stroke="var(--leaf-green)" stroke-width="2" stroke-dasharray="1.5 3" stroke-linecap="round"/>
      </svg>
    </div>
  </section>

  <section class="card card--back">
    <div class="contact">
      <div class="contact__name">Tamsin Corley</div>
      <div>Food &amp; Lifestyle coach</div>
      <div>tel: 0417382946</div>
      <div>eatwell@marovex.com</div>
    </div>
    <div class="appointment__label">your appointment is:</div>
    <div class="appointment__date">May 15th, 18.00 pm</div>
    <svg class="appointment__rule" width="300" height="6" viewBox="0 0 300 6">
      <line x1="0" y1="3" x2="298" y2="3" stroke="var(--paper)" stroke-width="2" stroke-dasharray="1.5 3" stroke-linecap="round"/>
    </svg>
  </section>
</body>
</html>
```